Stationery Design Project

KT7 Staffing requires letterhead and business card designs for a company based in London. Just like the name, we're a management resourcing company, providing resources to third party companies. You can see www.kt7staffing-example.com for ideas on existing colour schemes and design concepts that have been implimented and agreed to. Ultimately the design should broadcast professionalism, safety and the concept of growth.

Target Market(s)

Financial institutes; friendly societies (All UK based)

Industry/Entity Type

Safety

Requirements
Must have
• Files produced should be print ready; and the text in them editable (eg address, name etc)

```html
<!DOCTYPE html>
<html lang="en">
<head>
<meta charset="utf-8">
<title>KT7 Staffing – Business Card</title>
<link rel="stylesheet" href="https://fonts.googleapis.com/css2?family=Arimo:wght@400;700&display=swap">
<style>
  :root {
    --teal: #1d8b8e;
    --sky: #79bedf;
    --white: #ffffff;
    --page: #ffffff;
    --shadow: rgba(0, 0, 0, 0.28);
  }
  * { margin: 0; padding: 0; box-sizing: border-box; }
  html, body {
    width: 1200px;
    height: 900px;
    overflow: hidden;
    background: var(--page);
    font-family: "Arimo", Arial, sans-serif;
  }
  .canvas {
    position: relative;
    width: 1200px;
    height: 900px;
  }
  .card {
    position: absolute;
    background: var(--white);
    box-shadow: 4px 6px 10px var(--shadow);
    overflow: hidden;
  }

  /* Front */
  .card-front {
    left: 246px;
    top: 28px;
    width: 646px;
    height: 368px;
  }
  .holder-name {
    position: absolute;
    right: 22px;
    top: 16px;
    font-size: 37px;
    font-weight: 700;
    color: var(--teal);
    letter-spacing: -0.5px;
  }
  .contact-band {
    position: absolute;
    left: 0;
    top: 78px;
    width: 100%;
    height: 214px;
    background: var(--sky);
    padding: 30px 22px 0 0;
    text-align: right;
    color: var(--white);
    font-size: 27px;
    line-height: 37px;
    list-style: none;
  }
  .job-title { text-transform: uppercase; }
  .front-brand {
    position: absolute;
    left: 40px;
    top: 316px;
    display: flex;
    align-items: center;
    gap: 10px;
  }
  .front-brand .brand-square {
    width: 26px;
    height: 26px;
    background: var(--sky);
  }
  .front-brand .brand-name {
    font-size: 28px;
    font-weight: 700;
    color: var(--teal);
  }

  /* Back */
  .card-back {
    left: 264px;
    top: 504px;
    width: 648px;
    height: 368px;
  }
  .back-band {
    position: absolute;
    left: 0;
    width: 100%;
    height: 76px;
    background: var(--sky);
  }
  .back-band.top { top: 0; }
  .back-band.bottom { bottom: 0; }
  .back-brand {
    position: absolute;
    left: 0;
    right: 0;
    top: 76px;
    bottom: 76px;
    display: flex;
    align-items: center;
    justify-content: center;
    gap: 20px;
  }
  .back-brand .brand-square {
    width: 78px;
    height: 78px;
    background: var(--sky);
  }
  .back-brand .brand-name {
    font-size: 66px;
    font-weight: 700;
    color: var(--teal);
    letter-spacing: -1px;
  }
</style>
</head>
<body>
<main class="canvas">
  <section class="card card-front" aria-label="Business card front">
    <h1 class="holder-name">NAME NAME</h1>
    <ul class="contact-band">
      <li class="job-title">Job Title</li>
      <li class="email">name@kt7staffing-example.com</li>
      <li class="phone">p: 020.7946.0182</li>
      <li class="mobile">mp: 077.0090.0461</li>
    </ul>
    <div class="front-brand">
      <span class="brand-square"></span>
      <span class="brand-name">KT7 Staffing</span>
    </div>
  </section>

  <section class="card card-back" aria-label="Business card back">
    <div class="back-band top"></div>
    <div class="back-brand">
      <span class="brand-square"></span>
      <span class="brand-name">KT7 Staffing</span>
    </div>
    <div class="back-band bottom"></div>
  </section>
</main>
</body>
</html>
```